Organic Vanu (Coffee) Scrub Label for high end product

Need a product label for a coffee based body scrub called Vanu Body Scrub a 100% organic product. Our primary target is the yoga community so designs should reflect calm, perhaps incorporate eastern yoga symbology. simpler the better. Design should include both a round lid label and a rectangular wrap around label.

yoga community, people with cellulite, etc.

Community

```html
<!DOCTYPE html>
<html lang="en">
<head>
<meta charset="utf-8">
<title>Vanu Body Scrub – Lid Label</title>
<link href="https://fonts.googleapis.com/css2?family=Fredoka:wght@600&family=Lobster&display=swap" rel="stylesheet">
<style>
  :root {
    --canvas: #ffffff;
    --label-dark: #231f20;
    --coffee: #7b4d36;
    --coffee-deep: #5e3a28;
    --cream: #f6ec94;
    --gold: #c9a24a;
  }
  html, body {
    margin: 0;
    padding: 0;
    overflow: hidden;
    background: var(--canvas);
  }
  .canvas {
    width: 1200px;
    height: 1000px;
    position: relative;
    overflow: hidden;
    background: var(--canvas);
  }
  .lid-label {
    position: absolute;
    inset: 0;
    width: 1200px;
    height: 1000px;
  }
  .brand-name {
    font-family: "Fredoka", "Trebuchet MS", sans-serif;
    font-weight: 600;
    font-size: 118px;
    letter-spacing: 4px;
    fill: var(--coffee);
  }
  .product-script {
    font-family: "Lobster", "Brush Script MT", cursive;
    font-size: 215px;
  }
  .script-outer {
    fill: none;
    stroke: var(--label-dark);
    stroke-width: 30px;
    stroke-linejoin: round;
  }
  .script-glow {
    fill: var(--coffee);
    stroke: url(#goldStroke);
    stroke-width: 24px;
    stroke-linejoin: round;
    paint-order: stroke;
  }
  .script-inner {
    fill: var(--coffee);
    stroke: var(--coffee);
    stroke-width: 10px;
    stroke-linejoin: round;
    paint-order: stroke;
  }
</style>
</head>
<body>
<div class="canvas">
  <svg class="lid-label" viewBox="0 0 1200 1000" xmlns="http://www.w3.org/2000/svg">
    <defs>
      <clipPath id="labelDisc">
        <circle cx="600" cy="500" r="482"/>
      </clipPath>
      <radialGradient id="beanRing" cx="600" cy="500" r="482" gradientUnits="userSpaceOnUse">
        <stop offset="0.74" stop-color="#231f20" stop-opacity="0"/>
        <stop offset="0.84" stop-color="#6a4230" stop-opacity="0.85"/>
        <stop offset="1" stop-color="#7b4d36"/>
      </radialGradient>
      <linearGradient id="goldStroke" x1="0" y1="0" x2="1" y2="1">
        <stop offset="0" stop-color="#f8f0a0"/>
        <stop offset="0.5" stop-color="#f3e38a"/>
        <stop offset="1" stop-color="#c9a24a"/>
      </linearGradient>
      <linearGradient id="figureTone" x1="0" y1="0" x2="0" y2="1">
        <stop offset="0" stop-color="#7b4d36" stop-opacity="0.55"/>
        <stop offset="1" stop-color="#7b4d36" stop-opacity="0.3"/>
      </linearGradient>
    </defs>

    <g class="label-disc" clip-path="url(#labelDisc)">
      <circle cx="600" cy="500" r="482" fill="var(--label-dark)"/>
      <circle class="bean-border" cx="600" cy="500" r="482" fill="url(#beanRing)"
              role="img" aria-label="Border of scattered roasted coffee beans around the label edge"/>
    </g>

    <text class="brand-name" x="600" y="193" text-anchor="middle">VANU</text>

    <g class="product-title">
      <text class="product-script script-outer" x="318" y="408">Body</text>
      <text class="product-script script-glow" x="318" y="408">Body</text>
      <text class="product-script script-inner" x="318" y="408">Body</text>

      <text class="product-script script-outer" x="452" y="650">Scrub</text>
      <text class="product-script script-glow" x="452" y="650">Scrub</text>
      <text class="product-script script-inner" x="452" y="650">Scrub</text>
    </g>

    <rect class="yoga-figure" x="335" y="458" width="88" height="232" rx="30"
          fill="url(#figureTone)" role="img"
          aria-label="Small line drawing of a seated meditating yoga figure"/>
  </svg>
</div>
</body>
</html>
```